KettleMint.com Cooking Spice Jar Label Design

I need the following labels designed.

dimensions in inches. Drawings attached and logo attached

a. 3.5 oz wrap around spice label 2.3" tall x 3.3" wide
b. 5.5 oz warp around spice label 3.3" tall x 3.6" wide
c. 32 oz clear bottle. Flat label
c. flat label. 2.25 x 4
d. flat front of bottle label 5 x 3.5

Target Market(s)

gourmet cooks. restaurant managers. chefs. grocery store owners.

Industry/Entity Type

Cooking

Font styles to use
Other font styles liked:
• see attached logo

Requirements
Must have
• must be elegant and sophisticated using the existing logo attached.
• please look at www.kettlemint.com to see what the 3.5 oz label looks like today with the old logo.
Nice to have

```html
<!DOCTYPE html>
<html lang="en">
<head>
<meta charset="utf-8">
<title>KettleMint Celtic Gray Salt Label</title>
<link rel="stylesheet" href="https://fonts.googleapis.com/css2?family=Josefin+Sans:wght@300;400;600&display=swap">
<style>
  :root {
    --page: #ffffff;
    --label-white: #ffffff;
    --panel-top: #f5f5f5;
    --panel-bottom: #cbcccf;
    --heading-green: #8dc63f;
    --text-dark: #3d3d3d;
    --brand-grey: #434343;
    --olive: #6f8632;
    --amber: #f5a21c;
    --orange: #f26a2b;
    --brick: #c23a25;
    --white: #ffffff;
  }
  * { margin: 0; padding: 0; box-sizing: border-box; }
  html, body { width: 1200px; height: 876px; overflow: hidden; background: var(--page); }
  body { font-family: "Josefin Sans", sans-serif; color: var(--text-dark); }
  .label { position: relative; width: 1200px; height: 876px; }
  .label-art { position: absolute; inset: 0; }
  .info-block { position: absolute; text-align: center; }
  .info-block.left { left: 65px; width: 221px; }
  .info-heading {
    color: var(--heading-green);
    font-weight: 600;
    font-size: 13px;
    letter-spacing: 0;
    text-transform: uppercase;
    margin-bottom: 8px;
  }
  .info-text { font-size: 11px; line-height: 17px; font-weight: 400; }
  .info-text.large { font-size: 13px; line-height: 22px; font-weight: 300; }
  .usage { position: absolute; left: 944px; top: 112px; width: 195px; }
  .usage .info-heading { text-align: center; width: 190px; }
  .usage .info-text { text-align: left; }
  .brand-name {
    position: absolute;
    left: 300px; width: 620px; top: 270px;
    text-align: center;
    font-family: "Josefin Sans", sans-serif;
    font-weight: 400;
    font-size: 78px;
    color: var(--brand-grey);
  }
  .net-weight { position: absolute; left: 718px; top: 606px; font-size: 12px; font-weight: 300; }
  .product-name {
    position: absolute;
    left: 300px; width: 660px; top: 745px;
    text-align: center;
    color: var(--white);
    font-weight: 300;
    font-size: 50px;
    text-transform: uppercase;
  }
  .small-brand {
    position: absolute; left: 90px; top: 768px;
    font-size: 20px; font-weight: 400; color: var(--brand-grey);
  }
</style>
</head>
<body>
<main class="label">
  <svg class="label-art" viewBox="0 0 1200 876" width="1200" height="876" aria-hidden="true">
    <defs>
      <linearGradient id="panel-shade" x1="0" y1="0" x2="0" y2="1">
        <stop offset="0" stop-color="var(--panel-top)"/>
        <stop offset="1" stop-color="var(--panel-bottom)"/>
      </linearGradient>
      <linearGradient id="band-warm" x1="0" y1="0" x2="1" y2="0">
        <stop offset="0" stop-color="var(--brick)"/>
        <stop offset="0.5" stop-color="var(--orange)"/>
        <stop offset="1" stop-color="var(--brick)"/>
      </linearGradient>
      <linearGradient id="base-warm" x1="0" y1="0" x2="1" y2="0.3">
        <stop offset="0" stop-color="var(--orange)"/>
        <stop offset="0.6" stop-color="var(--orange)"/>
        <stop offset="1" stop-color="var(--brick)"/>
      </linearGradient>
    </defs>
    <rect class="label-ground" x="65" y="66" width="1080" height="755" fill="var(--label-white)"/>
    <rect class="side-panel" x="65" y="82" width="221" height="739" fill="url(#panel-shade)"/>
    <rect class="side-panel" x="925" y="82" width="220" height="739" fill="url(#panel-shade)"/>
    <rect class="top-band" x="65" y="66" width="1080" height="12" fill="url(#band-warm)"/>
    <rect class="top-line" x="65" y="78" width="1080" height="2" fill="var(--amber)"/>
    <rect class="top-line" x="65" y="80" width="1080" height="2" fill="var(--olive)"/>
    <path class="wave-olive" d="M65 620 C260 680 420 725 560 715 C760 700 950 610 1145 618 V821 H65 Z" fill="var(--olive)"/>
    <path class="wave-amber" d="M65 634 C260 694 420 739 560 729 C760 714 950 624 1145 632 V821 H65 Z" fill="var(--amber)"/>
    <path class="wave-base" d="M65 642 C260 702 420 747 560 737 C760 722 950 632 1145 640 V821 H65 Z" fill="url(#base-warm)"/>
  </svg>

  <section class="info-block left" style="top:112px">
    <h2 class="info-heading">Ingredients</h2>
    <p class="info-text">Place to add any description<br>of the product.</p>
  </section>
  <section class="info-block left" style="top:204px">
    <h2 class="info-heading">Cautions</h2>
    <p class="info-text">Place to add any other description<br>of the product.</p>
  </section>
  <section class="info-block left" style="top:310px">
    <h2 class="info-heading">Manufactured by</h2>
    <p class="info-text large">Place to add company detail<br>Name, address of company.</p>
  </section>
  <section class="info-block left" style="top:434px">
    <h2 class="info-heading">Customer care</h2>
    <p class="info-text large">Place to add company detail<br>Name, address of company.</p>
  </section>

  <section class="usage">
    <h2 class="info-heading">Usage instruction</h2>
    <p class="info-text">Place to add how to use the product:<br>1. Step one - This is step one how to use the product.<br>2. Step two- This is second step how to use the product.<br>3. Step three- This is third step how to use the product.</p>
  </section>

  <h1 class="brand-name">KettleMint</h1>
  <p class="net-weight">Netto 120 gram</p>
  <p class="product-name">Celtic Gray Salt</p>
  <p class="small-brand">KettleMint</p>
</main>
</body>
</html>
```